Cafe Menu Required

We need a menu for our coffee shop.
I would like something very much the same as what I have attached.

I have attached a word doc with the items needed on the menu.

I have also attached our logo

I would like to print these on A3 size poster

Industry/Entity Type

Cafe

```html
<!DOCTYPE html>
<html lang="en">
<head>
<meta charset="utf-8">
<title>Cafe Menu</title>
<link rel="stylesheet" href="https://fonts.googleapis.com/css2?family=Source+Sans+3:wght@400;700&display=swap">
<style>
  :root {
    --sky-deep: #0b1330;
    --sky-mid: #1e2a5e;
    --sky-violet: #4a3a7a;
    --menu-blue: #22a6ec;
    --rule-blue: #1f7fc4;
    --white: #ffffff;
    --title-white: #e9e9f2;
    --brand-red: #d8232a;
    --box-fill: rgba(40, 52, 120, 0.55);
    --box-line: #c9cbe0;
  }
  * { margin: 0; padding: 0; box-sizing: border-box; }
  html, body { width: 838px; height: 1200px; overflow: hidden; background: var(--sky-deep); }
  body { font-family: "Source Sans 3", "Myriad Pro", sans-serif; }
  .menu {
    position: relative;
    width: 838px; height: 1200px; overflow: hidden;
  }
  .menu-backdrop {
    position: absolute; inset: 0;
    background:
      radial-gradient(ellipse 60% 35% at 35% 8%, rgba(120, 90, 170, 0.75), transparent 70%),
      radial-gradient(ellipse 50% 30% at 85% 12%, rgba(110, 70, 150, 0.6), transparent 70%),
      radial-gradient(ellipse 55% 40% at 50% 60%, rgba(40, 60, 130, 0.55), transparent 75%),
      linear-gradient(180deg, var(--sky-violet) 0%, var(--sky-mid) 35%, var(--sky-deep) 100%);
  }
  .headline {
    position: absolute; left: 92px; top: 40px;
    font-weight: 700; font-size: 46px; line-height: 43px;
    color: var(--title-white); letter-spacing: 0.2px;
  }
  .brand-mark {
    position: absolute; left: 594px; top: 46px;
    width: 150px; height: 150px; border-radius: 50%;
    background: var(--brand-red);
    display: flex; align-items: center; justify-content: center;
  }
  .brand-name {
    font-weight: 700; font-size: 46px; color: var(--white); letter-spacing: 1px;
  }
  .section-title {
    position: absolute;
    font-size: 24px; font-weight: 400; color: var(--white);
    padding-bottom: 1px; border-bottom: 2px solid var(--white);
    line-height: 28px;
  }
  .price-list { position: absolute; list-style: none; }
  .price-list li {
    display: flex; justify-content: space-between; align-items: flex-end;
    color: var(--menu-blue); font-size: 21px; line-height: 29px;
    border-bottom: 1px solid var(--rule-blue);
  }
  .hot-list { left: 92px; top: 256px; width: 476px; }
  .hot-list li { height: 30.2px; }
  .extras-list { left: 90px; top: 800px; width: 256px; }
  .cold-list { left: 430px; top: 800px; width: 334px; }
  .extras-list li, .cold-list li { height: 32px; }
  .extras-list li.split { border-bottom: none; }
  .feature-box {
    position: absolute; top: 996px; height: 106px;
    border: 1.5px solid var(--box-line); background: var(--box-fill);
    color: var(--white); font-size: 19px; line-height: 24px;
    padding: 6px 10px 0 10px;
  }
  .feature-box .price { position: absolute; right: 10px; top: 6px; }
  .signature-drink { left: 90px; width: 256px; }
  .juice-bar { left: 436px; width: 326px; }
  .social {
    position: absolute; left: 124px; top: 1140px;
    display: flex; gap: 22px; align-items: center;
    color: var(--white); font-size: 16px;
  }
  .social-item { display: flex; align-items: center; gap: 6px; }
  .social-item .dot { width: 14px; height: 14px; background: var(--menu-blue); }
  .handle {
    position: absolute; right: 88px; top: 1142px;
    color: var(--white); font-size: 18px;
  }
</style>
</head>
<body>
<main class="menu">
  <div class="menu-backdrop" role="img" aria-label="Starry night sky with a purple and blue galaxy nebula"></div>

  <h1 class="headline">COFFEE<br>CATERING<br>FOOD TO GO</h1>

  <div class="brand-mark"><span class="brand-name">NOVA</span></div>

  <h2 class="section-title" style="left:92px; top:206px; width:192px;">HOT BEVERAGES</h2>
  <ul class="price-list hot-list">
    <li><span>Espresso</span><span>3.5</span></li>
    <li><span>Piccolo</span><span>3.5</span></li>
    <li><span>Short Macchiato</span><span>4.0</span></li>
    <li><span>Long Macchiato</span><span>4.5</span></li>
    <li><span>Latte</span><span>4&nbsp; / &nbsp;4.5&nbsp; / &nbsp;5.5</span></li>
    <li><span>Cappucinno</span><span>4&nbsp; / &nbsp;4.5&nbsp; / &nbsp;5.5</span></li>
    <li><span>Flat White</span><span>4&nbsp; / &nbsp;4.50&nbsp; / &nbsp;5.50</span></li>
    <li><span>Long Black</span><span>4&nbsp; / &nbsp;4.50&nbsp; / &nbsp;5.50</span></li>
    <li><span>Hot Chocolate</span><span>4&nbsp; / &nbsp;4.50&nbsp; / &nbsp;5.50</span></li>
    <li><span>White Hot Chocolate</span><span>4&nbsp; / &nbsp;4.50&nbsp; / &nbsp;5.50</span></li>
    <li><span>Mocha</span><span>4.5&nbsp; / &nbsp;5.0&nbsp; / &nbsp;6.0</span></li>
    <li><span>White Choc Mocha</span><span>4.5&nbsp; / &nbsp;5.0&nbsp; / &nbsp;6.0</span></li>
    <li><span>Chai Latte</span><span>4.5&nbsp; / &nbsp;5.0&nbsp; / &nbsp;6.0</span></li>
    <li><span>Dirty Chai</span><span>5.0&nbsp; / &nbsp;5.5&nbsp; / &nbsp;6.5</span></li>
    <li><span>Selection of Teas</span><span>3.8</span></li>
  </ul>

  <h2 class="section-title" style="left:90px; top:732px; width:96px;">EXTRAS</h2>
  <ul class="price-list extras-list" style="top:772px;">
    <li><span>Extra Shot</span><span>0.5</span></li>
    <li><span>Decaf</span><span>0.5</span></li>
    <li class="split"><span>Syrups – Caramel/</span><span></span></li>
    <li><span>Hazelnut/Vanilla</span><span>0.5</span></li>
    <li><span>Soy</span><span>0.5</span></li>
    <li><span>Lactose free</span><span>0.5</span></li>
  </ul>

  <h2 class="section-title" style="left:431px; top:732px; width:222px;">COLD BEVERAGES</h2>
  <ul class="price-list cold-list" style="top:772px;">
    <li><span>Iced Latte</span><span>4.5</span></li>
    <li><span>Iced Long Black</span><span>4.5</span></li>
    <li><span>Iced Coffee w/ice cream</span><span>6.0</span></li>
    <li><span>Iced Chocolate w/ice cream</span><span>6.0</span></li>
    <li><span>Coffee Frappe</span><span>6.0</span></li>
    <li><span>Mango Frappe</span><span>6.0</span></li>
  </ul>

  <div class="feature-box signature-drink">
    <span class="price">6</span>
    The nightcap<br>2 shots of espresso, a<br>generous scoop of<br>vanilla ice cream and milk
  </div>

  <div class="feature-box juice-bar">
    <span class="price">5</span>
    From the juice bar<br>create your own orange<br>apple carrot celery kale<br>spinach ginger beets lemon
  </div>

  <div class="social">
    <span class="social-item"><span class="dot"></span>Friendly</span>
    <span class="social-item"><span class="dot"></span>Chirpy</span>
    <span class="social-item"><span class="dot"></span>Snapbox</span>
  </div>
  <div class="handle">@nightbrewcoffee</div>
</main>
</body>
</html>
```